Business card design for Automotive workshop

We need a business card for a new automotive repair and tyre shop called Ridgeback Prime Automotive located in New Zealand. We are a clean, modern and fresh workshop and company.

Front needs to feature logo,
my name:
Lachie Westergaard (director)

Address:
48 Marlow Lane
Whitianga 3510

Phone: 07 842 1937
Mobile: 027 519 2764
Email: office@ridgebackmotors.co.nz
Website: ridgebackmotors.co.nz

Back needs to feature an area to write down appointment details, date and time.

Also feature a list of jobs and work we do such as,
Vehicle Servicing
All Mechanical Repairs
Warrant of Fitness
Tyres & Wheel Alignments
Automotive Diagnostics
Automotive Parts & Supplies

```html
<!DOCTYPE html>
<html lang="en">
<head>
<meta charset="utf-8">
<title>Ridgeback Prime Automotive – Business Card</title>
<link href="https://fonts.googleapis.com/css2?family=Raleway:wght@300;400;500;700&display=swap" rel="stylesheet">
<style>
  :root {
    --bg: #232428;
    --card: #ffffff;
    --red: #e31b23;
    --ink: #1b1b1b;
    --muted: #3a3a3a;
  }
  * { box-sizing: border-box; margin: 0; padding: 0; }
  html, body { width: 1200px; height: 900px; overflow: hidden; }
  body {
    background: var(--bg);
    font-family: "Raleway", sans-serif;
    color: var(--ink);
    position: relative;
  }
  .card {
    position: absolute;
    left: 280px;
    width: 640px;
    height: 414px;
    background: var(--card);
    overflow: hidden;
  }
  .card--back { top: 22px; }
  .card--front { top: 464px; }

  /* Brand name */
  .brand {
    display: flex;
    align-items: center;
    gap: 12px;
    color: var(--red);
    font-weight: 700;
    text-transform: uppercase;
    letter-spacing: 0.03em;
    white-space: nowrap;
  }
  .brand__mark { background: var(--red); flex: none; }

  /* Back */
  .card--back .brand { position: absolute; left: 40px; top: 52px; font-size: 19px; }
  .card--back .brand__mark { width: 14px; height: 14px; }
  .tread {
    position: absolute; right: 0; top: 0; width: 210px; height: 120px;
    background: linear-gradient(200deg, rgba(120,120,120,0.55), rgba(160,160,160,0.15) 60%, rgba(255,255,255,0) 85%);
  }
  .appointment {
    position: absolute; left: 40px; right: 40px; top: 140px;
    display: flex; gap: 14px; font-size: 15px; font-weight: 400; color: var(--muted);
  }
  .appointment__field { display: flex; align-items: flex-end; flex: 1; }
  .appointment__field--time { flex: 0.8; }
  .appointment__line { flex: 1; border-bottom: 1.5px dotted #777; margin: 0 0 4px 4px; }
  .services {
    position: absolute; left: 40px; right: 24px; top: 214px;
    list-style: none;
    display: grid; grid-template-columns: 200px 215px 1fr; row-gap: 26px; column-gap: 8px;
    font-size: 15px; font-weight: 400; color: var(--muted);
  }
  .services li { display: flex; align-items: center; gap: 10px; white-space: nowrap; }
  .services li::before {
    content: ""; width: 9px; height: 9px; border-radius: 50%; background: var(--red); flex: none;
  }
  .services__item--c1r1 { grid-column: 1; grid-row: 1; }
  .services__item--c1r2 { grid-column: 1; grid-row: 2; }
  .services__item--c1r3 { grid-column: 1 / span 2; grid-row: 3; }
  .services__item--c2r1 { grid-column: 2; grid-row: 1; }
  .services__item--c2r2 { grid-column: 2; grid-row: 2; }
  .services__item--c3r1 { grid-column: 3; grid-row: 1; }

  /* Front */
  .card--front .brand { position: absolute; left: 44px; top: 70px; font-size: 27px; }
  .card--front .brand__mark { width: 20px; height: 20px; }
  .person { position: absolute; left: 44px; top: 196px; }
  .person__name { font-size: 26px; font-weight: 700; letter-spacing: 0.01em; text-transform: uppercase; }
  .person__role { font-size: 19px; font-weight: 300; color: var(--muted); margin-top: 4px; }
  .rule { position: absolute; left: 44px; right: 44px; top: 272px; border-top: 1.5px solid var(--ink); }
  .contacts {
    position: absolute; left: 44px; right: 44px; top: 290px;
    display: flex; font-size: 16px; font-weight: 300; color: var(--ink);
  }
  .contacts__col { display: flex; flex-direction: column; gap: 14px; }
  .contacts__col--main { padding-right: 22px; border-right: 1.5px solid var(--ink); }
  .contacts__col--web { padding-left: 22px; }
  .contact { display: flex; align-items: center; gap: 10px; white-space: nowrap; }
  .contact svg { width: 18px; height: 18px; flex: none; fill: var(--red); }
</style>
</head>
<body>

<section class="card card--back" aria-label="Card back: appointment details and services">
  <div class="brand"><span class="brand__mark"></span>Ridgeback Prime Automotive</div>
  <div class="tread" role="img" aria-label="Grey tyre tread marks with splatter"></div>
  <div class="appointment">
    <div class="appointment__field">Date<span class="appointment__line"></span></div>
    <div class="appointment__field appointment__field--time">Time<span class="appointment__line"></span></div>
  </div>
  <ul class="services">
    <li class="services__item--c1r1">Vehicle Servicing</li>
    <li class="services__item--c2r1">All Mechanical Repairs</li>
    <li class="services__item--c3r1">Warrant of Fitness</li>
    <li class="services__item--c1r2">Automotive Diagnostics</li>
    <li class="services__item--c2r2">Tyres &amp; Wheel Alignments</li>
    <li class="services__item--c1r3">Automotive Parts &amp; Supplies</li>
  </ul>
</section>

<section class="card card--front" aria-label="Card front: contact details">
  <div class="brand"><span class="brand__mark"></span>Ridgeback Prime Automotive</div>
  <div class="person">
    <div class="person__name">Lachie Westergaard</div>
    <div class="person__role">director</div>
  </div>
  <div class="rule"></div>
  <div class="contacts">
    <div class="contacts__col contacts__col--main">
      <div class="contact">48 Marlow Lane Whitianga 3510
        <svg viewBox="0 0 24 24" aria-hidden="true"><path d="M12 2a7 7 0 0 0-7 7c0 5 7 13 7 13s7-8 7-13a7 7 0 0 0-7-7zm0 9.5A2.5 2.5 0 1 1 12 6.5a2.5 2.5 0 0 1 0 5z"/></svg>
      </div>
      <div class="contact">027 519 2764 / 07 842 1937
        <svg viewBox="0 0 24 24" aria-hidden="true"><path d="M6.6 10.8a15.1 15.1 0 0 0 6.6 6.6l2.2-2.2a1 1 0 0 1 1-.25 11.4 11.4 0 0 0 3.6.57 1 1 0 0 1 1 1V20a1 1 0 0 1-1 1A17 17 0 0 1 3 4a1 1 0 0 1 1-1h3.5a1 1 0 0 1 1 1c0 1.25.2 2.45.57 3.57a1 1 0 0 1-.25 1z"/></svg>
      </div>
    </div>
    <div class="contacts__col contacts__col--web">
      <div class="contact">
        <svg viewBox="0 0 24 24" aria-hidden="true"><path d="M3 5h18v14H3zm2 2v.5l7 5 7-5V7l-7 5z"/></svg>
        office@ridgebackmotors.co.nz
      </div>
      <div class="contact">
        <svg viewBox="0 0 24 24" aria-hidden="true"><path d="M12 2a10 10 0 1 0 0 20 10 10 0 0 0 0-20zm6.9 9h-3a15 15 0 0 0-1.3-6A8 8 0 0 1 18.9 11zM12 4c.9 1.2 1.8 3.6 1.9 7h-3.8C10.2 7.6 11.1 5.2 12 4zM9.4 5a15 15 0 0 0-1.3 6h-3A8 8 0 0 1 9.4 5zM5.1 13h3a15 15 0 0 0 1.3 6A8 8 0 0 1 5.1 13zM12 20c-.9-1.2-1.8-3.6-1.9-7h3.8c-.1 3.4-1 5.8-1.9 7zm2.6-1a15 15 0 0 0 1.3-6h3a8 8 0 0 1-4.3 6z"/></svg>
        ridgebackmotors.co.nz
      </div>
    </div>
  </div>
</section>

</body>
</html>
```